Thornfield Marsh, LLC Website

We are a small law firm in need of a website that contains the following:
1. Attractive main page
2. About us/attorney info for three people: Leonard Thornfield (attorney), Brent Marsh (attorney), and Melinda Carrow (legal assistant). We have bio's ready to submit.
3. Blog/video page. We'd like to post blogs and videos to help drive traffic
4. Multidistrict Litigation and Class Actions page, where we post information regarding active MDLs and Class actions that we are doing intake on.
Updates

Can you also please use the color "gold" in the design and logo? Thanks.

Industry/Entity Type

Legal

Coding

Coded - Design and coding required

Number of Pages Required

1 page

Colors
0054AA
0677BA
7BADD7
CADEEF
E8F1F8

Requirements
Must have
• 1. Attractive main page 2. About us/attorney info for three people: Leonard Thornfield (attorney), Brent Marsh (attorney), and Melinda Carrow (legal assistant). We have bio's ready to submit. 3. Blog/video page. We'd like to post blogs and videos to help drive traffic 4. Multidistrict Litigation and Class Actions page, where we post information regarding active MDLs and Class actions that we are doing intake on.

```html
<!DOCTYPE html>
<html lang="en">
<head>
<meta charset="utf-8">
<title>Thornfield Marsh, LLC — Lawyers</title>
<link href="https://fonts.googleapis.com/css2?family=Prata&family=DM+Sans:wght@400;500;600;700&display=swap" rel="stylesheet">
<style>
:root{
  --navy:#182b4d;
  --navy-line:#5b6d8d;
  --gold:#b8924f;
  --gold-soft:#c9a76a;
  --ink:#1c2a44;
  --text:#4a4f5a;
  --muted:#8a8f98;
  --paper:#ffffff;
  --mist:#efefef;
  --rule:#e3e3e3;
}
*{box-sizing:border-box;margin:0;padding:0}
html,body{width:1200px;height:3876px;overflow:hidden}
body{position:relative;background:var(--paper);font-family:"DM Sans",sans-serif;color:var(--text)}
.serif{font-family:"Prata",serif;font-weight:400}
.abs{position:absolute}
.btn{position:absolute;display:flex;align-items:center;justify-content:center;font-size:11px;font-weight:600;color:#fff}
.btn-gold{background:var(--gold)}
.btn-navy{background:var(--navy)}
.ph{position:absolute}

/* header */
.site-header{position:absolute;left:0;top:0;width:1200px;height:62px;background:#fff}
.brand{position:absolute;left:105px;top:15px;height:33px;display:flex;align-items:center;gap:8px}
.brand-mark{width:14px;height:14px;background:var(--gold)}
.brand-name{font-family:"DM Sans",sans-serif;font-weight:700;font-size:15px;color:var(--navy);letter-spacing:.3px}
.nav a{position:absolute;top:24px;font-size:10px;font-weight:500;color:var(--ink);text-decoration:none}
.nav a.active{color:var(--gold)}
.nav-underline{position:absolute;left:401px;top:60px;width:48px;height:2px;background:var(--gold)}
.header-phone{position:absolute;left:823px;top:22px;font-size:12px;font-weight:600;color:var(--ink);display:flex;gap:6px;align-items:center}

/* hero */
.hero{position:absolute;left:0;top:62px;width:1200px;height:469px;background:linear-gradient(100deg,#e6e7ea 0%,#f4f4f3 40%,#eceae3 65%,#c6ccd8 100%)}
.hero-title{position:absolute;left:0;top:128px;width:1200px;text-align:center;font-size:58px;line-height:72px;color:var(--navy)}

/* about */
.about-photo{left:105px;top:632px;width:250px;height:158px;border-radius:125px/79px;background:linear-gradient(135deg,#9aa3b0,#d6d9de 60%,#7c8594)}
.years{position:absolute;left:157px;top:808px;display:flex;align-items:center;gap:12px}
.years-num{font-size:40px;color:var(--navy)}
.years-label{font-size:10px;line-height:12px;color:var(--ink);font-weight:500}
.about-title{left:406px;top:628px;font-size:60px;line-height:72px;color:var(--navy)}
.about-copy{left:818px;top:660px;width:260px;font-size:10.5px;line-height:19px;color:var(--ink)}
.about-rule{left:818px;top:766px;width:325px;height:1px;background:var(--rule)}

/* stats */
.navy-band{left:0;top:1017px;width:1200px;height:673px;background:var(--navy)}
.stats{left:368px;top:938px;width:832px;height:155px;background:var(--gold)}
.stat-div{position:absolute;top:32px;width:1px;height:92px;background:rgba(255,255,255,.5)}
.stat{position:absolute;top:38px;color:#fff}
.stat-num{font-size:44px;line-height:48px}
.stat-label{font-size:9.5px;line-height:11px;margin-top:4px}

/* services */
.section-title{position:absolute;left:0;width:1200px;text-align:center;font-size:42px;line-height:55px}
.svc{position:absolute;top:1310px;width:482px;height:236px;border:1px solid var(--navy-line)}
.svc-img{position:absolute;left:0;top:0;width:182px;height:236px}
.svc-body{position:absolute;left:212px;top:32px;width:240px;color:#fff}
.svc-body h3{font-family:"Prata",serif;font-weight:400;font-size:20px;margin-bottom:20px}
.svc-body p{font-size:10px;line-height:19px;color:#e5e8ee}
.circle-arrow{position:absolute;left:212px;top:170px;width:30px;height:30px;border:1px solid var(--gold);border-radius:50%}

/* team */
.team-band{left:0;top:1690px;width:1200px;height:739px;background:var(--mist)}
.member{position:absolute;top:1906px;width:250px}
.member-photo{width:250px;height:311px}
.member-icons{position:absolute;left:97px;top:300px;display:flex;gap:8px}
.member-icons span{width:22px;height:22px;border-radius:50%;background:var(--navy);border:2px solid #fff}
.member-name{margin-top:30px;text-align:center;font-family:"Prata",serif;font-size:14px;color:var(--ink)}
.member-role{margin-top:6px;text-align:center;font-size:9px;color:var(--gold)}

/* testimonials */
.voices{left:0;top:2429px;width:1200px;height:453px;background:var(--gold)}
.voices-title{left:200px;top:2502px;font-size:44px;line-height:56px;color:#fff}
.avatar{position:absolute;top:2643px;width:68px;height:68px;border-radius:50%;border:3px solid rgba(255,255,255,.35)}
.quote{left:505px;top:2646px;width:480px;font-size:10.5px;line-height:19px;color:#fff}
.arrow-btn{position:absolute;top:2776px;width:30px;height:30px;border-radius:50%;border:1px solid rgba(255,255,255,.8)}

/* blog */
.post{position:absolute;top:3097px;width:250px;height:298px;background:#fff;border:1px solid var(--rule)}
.post-img{width:248px;height:156px}
.post-date{position:absolute;left:18px;top:178px;font-size:9px;color:var(--gold)}
.post-title{position:absolute;left:18px;top:198px;width:215px;font-family:"Prata",serif;font-size:13px;line-height:19px;color:var(--ink)}
.post-more{position:absolute;left:18px;top:268px;font-size:9px;font-weight:700;color:var(--ink)}

/* footer */
.site-footer{left:0;top:3540px;width:1200px;height:336px;background:var(--navy)}
.f-small{font-size:12px;font-weight:600;color:#fff}
.f-circle{position:absolute;width:40px;height:40px;border-radius:50%;border:1px solid var(--navy-line)}
.f-label{font-size:12px;font-weight:600;color:var(--gold)}
.f-text{font-size:10px;line-height:16px;color:#fff}
.social{position:absolute;left:1062px;width:30px;height:30px;border-radius:50%;border:1px solid var(--navy-line)}
.footer-rule{left:105px;top:3805px;width:988px;height:1px;background:#2f4266}
.footer-nav span{position:absolute;top:3829px;font-size:10px;color:#fff}
</style>
</head>
<body>

<header class="site-header">
  <div class="brand"><span class="brand-mark"></span><span class="brand-name">THORNFIELD MARSH, LLC</span></div>
  <nav class="nav">
    <a class="active" style="left:411px">Home</a>
    <a style="left:455px">About Us</a>
    <a style="left:513px">Multidistrict Litigation</a>
    <a style="left:627px">Class Actions</a>
    <a style="left:705px">Blog</a>
    <a style="left:742px">Contact Us</a>
  </nav>
  <div class="nav-underline"></div>
  <div class="header-phone">
    <svg width="13" height="13" viewBox="0 0 24 24" fill="none" stroke="#1c2a44" stroke-width="2"><path d="M5 3h4l2 5-2.5 1.5a11 11 0 0 0 6 6L16 13l5 2v4a2 2 0 0 1-2 2A16 16 0 0 1 3 5a2 2 0 0 1 2-2z"/></svg>
    (555) 218-4470
  </div>
  <div class="btn btn-gold" style="left:956px;top:12px;width:137px;height:38px">Free Case Evaluation</div>
</header>

<section class="hero" role="img" aria-label="Lawyer's desk with gavel and golden scales of justice"></section>
<h1 class="serif hero-title" style="top:186px">A law firm with a<br>passion for sucesss</h1>
<div class="btn btn-gold" style="left:538px;top:365px;width:124px;height:37px;font-size:10px">Contcat Us Today!</div>

<div class="ph about-photo" role="img" aria-label="Three attorneys meeting around a table"></div>
<div class="years"><span class="serif years-num">25+</span><span class="years-label">Years<br>experiences</span></div>
<h2 class="serif abs about-title">We proudly<br>fight for your<br>rights</h2>
<p class="abs about-copy">Lorem Ipsum is simply dummy text of the printing and typesetting industry lorem Ipsum has been the industry's standard dummy text ever since the unknown.</p>
<div class="abs about-rule"></div>
<div class="btn btn-navy" style="left:818px;top:797px;width:105px;height:36px;font-size:10px">Discover More</div>

<div class="abs navy-band"></div>
<div class="abs stats">
  <div class="stat" style="left:121px"><div class="serif stat-num">1.3K+</div><div class="stat-label">Critical cases solved<br>successfully</div></div>
  <div class="stat-div" style="left:295px"></div>
  <div class="stat" style="left:373px"><div class="serif stat-num">55+</div><div class="stat-label">Established fact work<br>that reader</div></div>
  <div class="stat-div" style="left:548px"></div>
  <div class="stat" style="left:626px"><div class="serif stat-num">12+</div><div class="stat-label">standard dummy<br>achievement</div></div>
</div>

<h2 class="serif section-title" style="top:1168px;color:#fff">We are provided especially<br>services to you.</h2>
<div class="svc" style="left:105px">
  <div class="ph svc-img" role="img" aria-label="Hands holding a model building beside a gavel" style="background:linear-gradient(135deg,#d9a560,#f1e0c2 55%,#8a6a48)"></div>
  <div class="svc-body"><h3>Multidistrict Litigation</h3><p>Lorem Ipsum is simply dummy text of the work printing and typesetting industry lorem Ipsum has been the industry's standard dummy text ever since the unknown.</p></div>
  <div class="circle-arrow" style="left:212px"><svg width="28" height="28" viewBox="0 0 28 28"><path d="M11 17l6-6M12 11h5v5" stroke="#fff" fill="none" stroke-width="1.2"/></svg></div>
</div>
<div class="svc" style="left:612px">
  <div class="ph svc-img" role="img" aria-label="Gavel, pen and scales on a desk" style="background:linear-gradient(135deg,#ece8e2,#c9b59a 55%,#6e4a33)"></div>
  <div class="svc-body"><h3>Class Actions</h3><p>Lorem Ipsum is simply dummy text of the work printing and typesetting industry lorem Ipsum has been the industry's standard dummy text ever since the unknown.</p></div>
  <div class="circle-arrow" style="left:212px"><svg width="28" height="28" viewBox="0 0 28 28"><path d="M11 17l6-6M12 11h5v5" stroke="#fff" fill="none" stroke-width="1.2"/></svg></div>
</div>
<div class="btn btn-gold" style="left:531px;top:1579px;width:137px;height:36px;font-size:10px">Free Case Evaluation</div>

<div class="abs team-band"></div>
<h2 class="serif section-title" style="top:1762px;color:var(--navy)">We provide our advance level<br>of legal support</h2>
<div class="member" style="left:200px">
  <div class="member-photo" role="img" aria-label="Portrait of attorney Leonard Thornfield" style="background:linear-gradient(160deg,#e9dcc1,#b8a98a 60%,#3a3a3e)"></div>
  <div class="member-icons"><span></span><span></span></div>
  <div class="member-name">Leonard Thornfield</div><div class="member-role">Attorney</div>
</div>
<div class="member" style="left:475px">
  <div class="member-photo" role="img" aria-label="Portrait of attorney Brent Marsh" style="background:linear-gradient(160deg,#6f6a5e,#3d4540 60%,#1f3a3a)"></div>
  <div class="member-icons"><span></span><span></span></div>
  <div class="member-name">Brent Marsh</div><div class="member-role">Attorney</div>
</div>
<div class="member" style="left:750px">
  <div class="member-photo" role="img" aria-label="Portrait of legal assistant Melinda Carrow" style="background:linear-gradient(160deg,#dfe6ec,#aebdca 55%,#25334f)"></div>
  <div class="member-icons"><span></span><span></span></div>
  <div class="member-name">Melinda Carrow</div><div class="member-role">legal Assistant</div>
</div>
<div class="btn btn-navy" style="left:549px;top:2318px;width:101px;height:36px;font-size:10px">Explore More</div>

<div class="abs voices"></div>
<h2 class="serif abs voices-title">What people are<br>saying</h2>
<div class="avatar" role="img" aria-label="Client portrait" style="left:199px;background:#c9a97c"></div>
<div class="avatar" role="img" aria-label="Client portrait" style="left:294px;background:#e8d2b8;border-color:#fff"></div>
<div class="avatar" role="img" aria-label="Client portrait" style="left:387px;background:#c89c6e"></div>
<div class="abs serif" style="left:268px;top:2730px;width:120px;text-align:center;font-size:11px;color:#fff">Claire Whitmore</div>
<div class="abs" style="left:268px;top:2746px;width:120px;text-align:center;font-size:9px;color:#fff">Costumer</div>
<div class="abs quote"><p>Lorem ipsum is simply dummy text of the printing and typesetting industry. lorem ipsum has been the industry's standard dummy text ever since the 1500s, when an unknown printer took a galley of type and scrambled it to make a type specimen book.</p><p style="margin-top:12px;width:290px">Lorem ipsum is simply dummy text of the printing and typesetting industry lorem ipsum...</p></div>
<div class="arrow-btn" style="left:505px"><svg width="28" height="28" viewBox="0 0 28 28"><path d="M16 10l-4 4 4 4" stroke="#fff" fill="none" stroke-width="1.3"/></svg></div>
<div class="arrow-btn" style="left:543px"><svg width="28" height="28" viewBox="0 0 28 28"><path d="M12 10l4 4-4 4" stroke="#fff" fill="none" stroke-width="1.3"/></svg></div>

<h2 class="serif section-title" style="top:2953px;color:var(--navy)">Our advice to people.</h2>
<article class="post" style="left:200px">
  <div class="post-img" role="img" aria-label="Attorney signing documents at a desk" style="background:linear-gradient(135deg,#5a4a3e,#d8d1c6 60%,#f1ede7)"></div>
  <div class="post-date">Jan. 8, 2025</div>
  <div class="post-title">Contrary to popular belief, lorem ipsum is not simply random text classical latin</div>
  <div class="post-more">Read More ↗</div>
</article>
<article class="post" style="left:475px;border:none;background:linear-gradient(160deg,#3b4350,#6b7682 55%,#8d8a82)" role="img" aria-label="Video: consultation between an attorney and a client">
  <svg class="abs" style="left:112px;top:136px" width="26" height="26" viewBox="0 0 26 26"><circle cx="13" cy="13" r="13" fill="#fff"/><path d="M10 8l8 5-8 5z" fill="#182b4d"/></svg>
</article>
<article class="post" style="left:750px">
  <div class="post-img" role="img" aria-label="Lawyer holding coffee at a meeting table" style="background:linear-gradient(135deg,#f2f0ec,#b8bcc2 55%,#8a5a3a)"></div>
  <div class="post-date">Feb. 10, 2025</div>
  <div class="post-title">Contrary to popular belief, lorem ipsum is not simply random text classical latin</div>
  <div class="post-more">Read More ↗</div>
</article>
<div class="btn btn-navy" style="left:549px;top:3429px;width:101px;height:36px;font-size:10px">View All Blog</div>

<footer class="abs site-footer"></footer>
<div class="abs f-small" style="left:105px;top:3614px">Contact us</div>
<div class="abs serif" style="left:105px;top:3646px;font-size:40px;color:var(--gold)">Get in touch</div>
<p class="abs f-text" style="left:105px;top:3711px;width:340px;font-size:9.5px;line-height:15px">Lorem ipsum is simply dummy text of the printing and typesetting industry. lorem ipsum has been the industry's standard dummy text ever galley of type and type specimen book.</p>

<div class="f-circle" style="left:522px;top:3627px"><svg width="38" height="38" viewBox="0 0 38 38"><path d="M19 27s-6-6-6-10a6 6 0 0 1 12 0c0 4-6 10-6 10z" stroke="#b8924f" fill="none" stroke-width="1.2"/><circle cx="19" cy="17" r="2" stroke="#b8924f" fill="none"/></svg></div>
<div class="abs f-label" style="left:574px;top:3656px">Address</div>
<div class="abs f-text" style="left:574px;top:3680px">214 Harbor Row, Bayport,<br>AL 36000</div>
<div class="abs" style="left:574px;top:3722px;font-size:9px;font-weight:600;color:var(--gold)">Get Directions ↗</div>

<div class="f-circle" style="left:775px;top:3627px"><svg width="38" height="38" viewBox="0 0 38 38"><path d="M14 12h3l1.5 4-2 1a8 8 0 0 0 4.5 4.5l1-2 4 1.5v3a1.5 1.5 0 0 1-1.5 1.5A12 12 0 0 1 12.5 13.5 1.5 1.5 0 0 1 14 12z" stroke="#b8924f" fill="none" stroke-width="1.2"/></svg></div>
<div class="abs f-label" style="left:826px;top:3656px">Contact Details</div>
<div class="abs f-text" style="left:826px;top:3680px">hello@thornfieldmarsh.law</div>
<div class="abs" style="left:826px;top:3698px;font-size:13px;color:var(--gold)">(555) 218-4470</div>

<div class="social" style="top:3646px"></div>
<div class="social" style="top:3683px"></div>
<div class="social" style="top:3721px"></div>
<svg class="abs" style="left:1138px;top:3790px" width="18" height="20" viewBox="0 0 18 20"><path d="M9 1l8 18-8-5-8 5z" fill="#b8924f"/></svg>

<div class="abs footer-rule"></div>
<div class="abs" style="left:105px;top:3829px;font-size:9.5px;color:#fff">© 2025 <span style="color:var(--gold)">Thornfield Marsh.</span> All rights reserved</div>
<div class="footer-nav">
  <span style="left:523px;color:var(--gold)">Home</span>
  <span style="left:571px">About Us</span>
  <span style="left:632px">Multidistrict Litigation</span>
  <span style="left:752px">Class Actions</span>
  <span style="left:832px">Blog</span>
  <span style="left:873px">Contact Us</span>
</div>

</body>
</html>
```